We are looking for an effective ad to recruit work from home Loan Officers for our Mortgage Brokerage.
Use the following text...
Earn Mortgage Income in your sleep. Its as easy as 1, 2, 3.....
1) Solicit Potential Applicants (Word of Mouth, Email, Social Media etc.)
2) Take Complete Applications & Submit Them
3) Wait to Get Paid.......(Avg. $2,500 per closing)
"You open the door, we'll finish the deal"
No Experience Necessary
No Goals or Quotas
No Office Hours / Work from Home Office
...and We Fully Reimburse ALL LICENSING FEES!!
Email Resume to mwelby@brightharborloans.example
Bright Harbor Lending Group, Inc.
947 W Caldwell Avenue, #318
Baltimore, MD 21230
NMLS #731860
www.brightharborloans.example
Phone (800) 555-0142
Licensed Mortgage Broker in MD and DC since 1997
Target Market(s)
Professionals looking to earn part time income at Loan Officers, preferably with strong social media following.
Industry/Entity Type
Loan
Look and feel

```html
<!DOCTYPE html>
<html lang="en">
<head>
<meta charset="utf-8">
<title>Bright Harbor Lending Group – Loan Officer Recruitment Flyer</title>
<link href="https://fonts.googleapis.com/css2?family=Oswald:wght@500;600&family=Questrial&family=Open+Sans:wght@600;700&display=swap" rel="stylesheet">
<style>
  :root {
    --backdrop: #849c9c;
    --paper: #f7f7f5;
    --gold: #b9a027;
    --blue: #0f4c96;
    --ink: #1c1c1c;
    --photo-light: #f1ece2;
    --photo-warm: #d8b54a;
    --photo-deep: #8a5a33;
  }
  * { margin: 0; padding: 0; box-sizing: border-box; }
  html, body {
    width: 1200px; height: 960px; overflow: hidden;
    background: var(--backdrop);
  }
  .flyer {
    position: absolute; left: 283px; top: 30px;
    width: 634px; height: 900px;
    background: var(--paper);
    overflow: hidden;
    font-family: "Questrial", "Century Gothic", sans-serif;
    color: var(--ink);
  }
  .hero-photo {
    position: absolute; left: 0; top: 0; width: 535px; height: 404px;
    background: radial-gradient(ellipse at 45% 45%, var(--photo-deep) 0%, var(--photo-warm) 38%, var(--photo-light) 72%);
  }
  .hero-stripe { position: absolute; left: 0; top: 402px; }
  .corner-mark { position: absolute; left: 540px; top: 0; }
  .headline {
    position: absolute; left: 372px; top: 40px;
    font-family: "Oswald", "Arial Narrow", sans-serif; font-weight: 600;
    font-size: 98px; line-height: 1; letter-spacing: 1px;
    color: var(--gold);
  }
  .headline-box {
    position: absolute; left: 372px; top: 130px; width: 262px; height: 103px;
    background: var(--gold); color: #fff;
    padding: 10px 0 0 12px;
    font-family: "Oswald", "Arial Narrow", sans-serif; font-weight: 500;
    font-size: 20px; line-height: 1.22;
  }
  .steps { position: absolute; left: 20px; top: 442px; list-style: none; }
  .step {
    display: flex; align-items: center; height: 31px;
    font-size: 17px;
  }
  .step-badge {
    width: 22px; height: 18px; margin-right: 10px;
    background: var(--gold); color: #fff; font-size: 12px;
    display: flex; align-items: center; justify-content: center;
  }
  .motto-band {
    position: absolute; left: 0; top: 540px; width: 634px; height: 37px;
    background: var(--blue); color: #fff;
    font-family: "Open Sans", Arial, sans-serif; font-weight: 700;
    font-size: 21px; line-height: 37px; padding-left: 43px;
  }
  .perks { position: absolute; left: 45px; top: 594px; list-style: none; font-size: 15px; }
  .perks li { height: 23px; }
  .perks strong { color: var(--blue); font-family: "Open Sans", Arial, sans-serif; font-weight: 700; }
  .resume-bar {
    position: absolute; left: 260px; top: 713px; width: 374px; height: 29px;
    background: var(--gold); color: #fff;
    font-family: "Open Sans", Arial, sans-serif; font-weight: 600;
    font-size: 13px; line-height: 29px; padding-left: 24px;
  }
  .brand {
    position: absolute; left: 22px; top: 780px; width: 230px;
    display: flex; align-items: center; gap: 10px;
  }
  .brand-dot { flex: none; width: 30px; height: 30px; border-radius: 50%; background: var(--gold); }
  .brand-name { font-size: 17px; line-height: 1.2; color: var(--blue); }
  .contact {
    position: absolute; left: 285px; top: 760px;
    font-size: 13px; line-height: 18px;
  }
  .contact .company { font-family: "Open Sans", Arial, sans-serif; font-weight: 700; }
  .licensed { position: absolute; left: 285px; top: 868px; font-size: 13px; color: #333; }
</style>
</head>
<body>
  <main class="flyer">
    <div class="hero-photo" role="img" aria-label="Photo of a smiling young woman in a yellow top holding a fan of dollar bills"></div>
    <svg class="hero-stripe" width="522" height="16" viewBox="0 0 522 16"><polygon points="0,0 522,0 510,16 0,16" fill="var(--blue)"/></svg>
    <svg class="corner-mark" width="66" height="130" viewBox="0 0 66 130">
      <polygon points="0,0 66,0 33,34" fill="var(--gold)"/>
      <rect x="28" y="30" width="10" height="100" fill="var(--gold)"/>
    </svg>
    <h1 class="headline">EARN</h1>
    <p class="headline-box">Mortgage Income<br>in your sleep.<br>Its as easy as 1, 2, 3...</p>

    <ol class="steps">
      <li class="step"><span class="step-badge">1</span>Solicit Potential Applicants (Word of Mouth, Email, Social Media etc.)</li>
      <li class="step"><span class="step-badge">2</span>Take Complete Applications &amp; Submit Them</li>
      <li class="step"><span class="step-badge">3</span>Wait to Get Paid.......(Avg. $2,500 per closing)</li>
    </ol>

    <p class="motto-band">"You open the door, we'll finish the deal"</p>

    <ul class="perks">
      <li>No Experience Necessary</li>
      <li>No Goals or Quotas</li>
      <li>No Office Hours / Work from Home Office</li>
      <li>...and <strong>We Fully Reimburse ALL LICENSING FEES!!</strong></li>
    </ul>

    <p class="resume-bar">Email Resume to mwelby@brightharborloans.example</p>

    <div class="brand">
      <span class="brand-dot"></span>
      <span class="brand-name">Bright Harbor Lending Group, Inc.</span>
    </div>

    <address class="contact" style="font-style:normal">
      <span class="company">Bright Harbor Lending Group, Inc.</span><br>
      947 W Caldwell Avenue, #318<br>
      Baltimore, MD 21230<br>
      NMLS #731860<br>
      www.brightharborloans.example<br>
      Phone (800) 555-0142
    </address>
    <p class="licensed">Licensed Mortgage Broker in MD and DC since 1997</p>
  </main>
</body>
</html>
```